Bluefinch Painting needs a Website

We need a website built for a Painting company I own, we mainly do residential painting, but don't want to be limited to that.

Need to have estimate request form.
Need pic's of past projects

I like the look of the website for http://www.harborline-painters.example
& "Wexley Property inspections"

My logo that was designed here on ArtHive on the front page

I would like one of the houses I downloaded as part of the background
of the front page.

Target Market(s)

Home owners

Industry/Entity Type

Painting

Number of Pages Required

1 page

Font styles to use
Serif

Requirements
Must have
• Estimate request form for home owners to fill out -
• Name:
• Phone Number:
• Address:
• E-mail:
• Painting project description:
• And my info to:
• My phone number: (555) 318-7046
• My web address bluefinchpainting.example
Nice to have
• My logo that was designed here on ArtHive

```html
<!DOCTYPE html>
<html lang="en">
<head>
<meta charset="utf-8">
<title>Bluefinch Painting</title>
<link href="https://fonts.googleapis.com/css2?family=Roboto:wght@300;400;500;700&family=Open+Sans:ital,wght@0,400;0,600;0,700;1,400&display=swap" rel="stylesheet">
<style>
:root{
  --blue:#1b67a6;
  --blue-dark:#12548c;
  --green:#8cc863;
  --green-panel:#cfe6b7;
  --green-bright:#7dbf4d;
  --teal:#6fb1ad;
  --violet:#6f7fc4;
  --pink:#e86a9b;
  --cream:#f1efe4;
  --ink:#222;
  --body:#333;
  --footer:#474747;
  --white:#fff;
}
*{margin:0;padding:0;box-sizing:border-box}
html,body{width:1200px;height:2293px;overflow:hidden}
body{font-family:"Open Sans",Arial,sans-serif;color:var(--body);background:var(--white);position:relative}
.abs{position:absolute}
.rainbow{height:6px;background:linear-gradient(90deg,#6db3e4 0 20%,#e86a9b 20% 40%,#8cc863 40% 60%,#f2c94c 60% 80%,#6f7fc4 80% 100%)}

/* header */
.site-header{top:0;left:0;width:1200px;height:109px}
.brand{left:157px;top:30px;display:flex;align-items:center;gap:12px}
.brand-mark{width:44px;height:44px;background:var(--blue)}
.brand-name{font-family:"Roboto",sans-serif;font-weight:500;font-size:34px;color:var(--blue-dark);letter-spacing:1px}
.social{right:157px;top:28px;display:flex;gap:6px}
.social span{width:20px;height:20px;border-radius:50%;border:2px solid #5a8fc4}
.phone{right:157px;top:52px;display:flex;align-items:center;gap:10px;font-family:"Roboto",sans-serif;font-size:25px;color:var(--ink)}

/* nav */
.main-nav{top:109px;left:0;width:1200px;height:50px;background:var(--blue)}
.main-nav ul{list-style:none;position:absolute;left:157px;top:10px;display:flex;gap:8px}
.main-nav li{font-family:"Roboto",sans-serif;font-size:15px;color:var(--white);padding:6px 14px;height:30px}
.main-nav li.active{background:var(--green);width:82px;text-align:center}
.quote-btn{left:841px;top:8px;width:200px;height:34px;background:var(--green);display:flex;align-items:center;justify-content:flex-end;padding-right:14px;font-family:"Roboto",sans-serif;font-weight:700;font-size:14px;color:#1d2a12}
.quote-btn i{position:absolute;left:0;top:0;width:34px;height:34px;background:#1f2a33}

/* hero */
.hero{top:159px;left:0;width:1200px;height:357px;background:linear-gradient(180deg,#8fae7e 0%,#b8a993 45%,#7d7a74 75%,#5a6b4a 100%)}
.hero-caption{left:0;bottom:13px;width:560px;height:40px;background:rgba(40,40,40,.45);padding-left:166px;font-family:"Roboto",sans-serif;font-size:25px;color:var(--white);line-height:40px}
.hero .rainbow{position:absolute;bottom:0;left:0;width:100%}

/* welcome */
.welcome{top:516px;left:0;width:1200px;height:224px;text-align:center}
.welcome h1{position:absolute;top:40px;width:100%;font-family:"Roboto",sans-serif;font-weight:400;font-size:30px;color:var(--ink)}
.welcome p{position:absolute;top:80px;left:195px;width:810px;font-size:11.5px;line-height:1.7;color:#444}
.btn{display:inline-block;background:var(--blue);color:var(--white);font-family:"Roboto",sans-serif;font-weight:500;font-size:12px;text-transform:uppercase;text-align:center;line-height:32px;height:32px;width:104px}
.welcome .btn{position:absolute;left:548px;top:153px}

/* services */
.services{top:740px;left:0;width:1200px;height:307px;background:var(--cream)}
.service{width:210px;height:210px;top:53px;text-align:center}
.service svg{position:absolute;left:0;top:0}
.service .service-label{position:absolute;left:0;top:122px;width:210px;text-align:center;font-family:"Roboto",sans-serif;font-size:18px;color:#333}

/* feature */
.feature{top:1047px;left:0;width:1200px;height:377px;background:var(--green)}
.feature .pointer{position:absolute;left:248px;top:-20px;border:20px solid transparent;border-top:0;border-bottom-color:var(--green)}
.feature-panel{left:157px;top:38px;width:881px;height:300px;background:var(--green-panel)}
.feature-panel h3{position:absolute;left:15px;top:18px;font-family:"Roboto",sans-serif;font-weight:300;font-size:27px;color:#222;line-height:1}
.feature-panel h2{position:absolute;left:13px;top:44px;font-family:"Roboto",sans-serif;font-weight:300;font-size:64px;color:#111;line-height:1}
.feature-panel p{position:absolute;left:15px;top:108px;width:425px;font-size:10.5px;line-height:14.5px;color:#222}
.feature-panel .btn{position:absolute;left:15px;top:248px}
.feature-photo{left:456px;top:18px;width:411px;height:261px;background:linear-gradient(135deg,#e9ecef 0%,#c9ced3 50%,#a0a6ab 100%)}

/* projects */
.projects{top:1424px;left:0;width:1200px;height:380px}
.section-title{font-family:"Roboto",sans-serif;font-weight:400;font-size:22px;color:#222;text-transform:uppercase}
.projects .section-title{position:absolute;top:34px;width:100%;text-align:center}
.project{top:72px;width:210px}
.project-img{height:96px}
.project h4{margin-top:14px;font-family:"Roboto",sans-serif;font-weight:700;font-size:11.5px;color:#111}
.project p{margin-top:5px;font-size:11px;font-style:italic;line-height:1.55;color:#444}
.project .btn{position:absolute;top:233px;left:0}
.project .btn.muted{background:#a5a5a5}
.arrow{top:172px}

/* news */
.news{top:1804px;left:0;width:1200px;height:384px;background:linear-gradient(180deg,#eceef0,#e3e6e9)}
.news .section-title{position:absolute;left:162px;top:58px;font-size:25px}
.news-arrows{left:690px;top:60px;display:flex;gap:6px}
.news-item{width:280px;height:80px}
.news-date{position:absolute;left:0;top:0;width:40px;text-align:center}
.news-date b{display:block;font-family:"Roboto",sans-serif;font-weight:700;font-size:24px;color:#111;line-height:32px;background:var(--white)}
.news-date small{display:block;background:#8a8a8a;color:var(--white);font-size:9px;line-height:18px}
.news-item h5{position:absolute;left:55px;top:0;font-family:"Roboto",sans-serif;font-weight:700;font-size:11.5px;color:#111}
.news-item p{position:absolute;left:55px;top:17px;width:225px;font-size:11px;font-style:italic;line-height:1.4;color:#333}
.news-item a{position:absolute;left:55px;top:66px;font-size:11px;color:var(--blue);text-decoration:none;font-weight:600}
.news-rule{left:162px;top:197px;width:580px;height:1px;background:#c9ccd0}
.quick-contact{left:751px;top:42px;width:279px;height:292px;background:var(--blue);border-radius:4px;padding:18px 20px}
.quick-contact h3{font-family:"Roboto",sans-serif;font-weight:400;font-size:25px;color:var(--white);margin-bottom:12px}
.quick-contact input,.quick-contact textarea{display:block;width:100%;height:30px;border:0;border-radius:2px;margin-bottom:7px;padding:0 8px;font-family:"Open Sans",sans-serif;font-size:11px;color:#777}
.quick-contact textarea{height:64px;padding-top:6px;resize:none}
.quick-contact button{margin-top:10px;width:90px;height:28px;border:0;background:var(--green-bright);color:#12330a;font-family:"Roboto",sans-serif;font-weight:700;font-size:12px}

/* footer */
.site-footer{top:2188px;left:0;width:1200px;height:105px;background:var(--footer);text-align:center}
.site-footer .social{position:absolute;left:553px;top:30px}
.site-footer .social span{border-color:#ddd}
.site-footer p{position:absolute;top:62px;width:100%;font-size:11.5px;color:#e6e6e6}
.site-footer .rainbow{position:absolute;bottom:0;left:0;width:100%}
</style>
</head>
<body>

<div class="abs rainbow" style="top:0;left:0;width:1200px;height:5px;z-index:2"></div>

<header class="abs site-header">
  <div class="abs brand"><span class="brand-mark"></span><span class="brand-name">Bluefinch Painting</span></div>
  <div class="abs social"><span></span><span></span><span></span><span></span></div>
  <div class="abs phone">
    <svg width="18" height="22" viewBox="0 0 18 22"><path d="M4 1 L8 1 L9 6 L6 8 Q8 13 11 15 L13 12 L17 14 L17 18 Q14 22 9 18 Q2 11 2 4 Z" fill="#1b67a6"/></svg>
    (555) 318-7046
  </div>
</header>

<nav class="abs main-nav">
  <ul>
    <li class="active">HOME</li>
    <li>ABOUT US</li>
    <li>SERVICES</li>
    <li>PROJECTS</li>
    <li>CONTACT US</li>
  </ul>
  <div class="abs quote-btn"><i></i>GET A FREE QUOTE</div>
</nav>

<section class="abs hero" role="img" aria-label="Photo of a two-storey house with a pickup truck and branded work trailer parked in front">
  <div class="abs hero-caption">CREATE YOUR WORLD WITH US</div>
  <div class="rainbow"></div>
</section>

<section class="abs welcome">
  <h1>Welcome to Bluefinch Painting</h1>
  <p>Sed ut perspiciatis unde omnis iste natus error sit voluptatem accudf dgsantium doloremque laudantium, totam rem aperiam, eaque ipsa quae ab illo inventore veritatis et quasi architecto beatae vitae dicta sunt explicabo. Nemo enim ipsam voluptatem quia voluptas sit aspernatur aut odit aut fudgit, sed quia cfdonsequ untur magni dolores eos qui ratione voluptatem sequi nesdfciunt. Neque porro quisquam est, qui dolorem.</p>
  <span class="btn">Read More</span>
</section>

<section class="abs services">
  <div class="abs service" style="left:159px">
    <svg width="210" height="210"><circle cx="105" cy="105" r="92" fill="none" stroke="#8cc863" stroke-width="14"/>
      <path d="M82 82 L105 62 L128 82 L128 104 L82 104 Z" fill="#7dbf4d"/><rect x="100" y="88" width="10" height="16" fill="#fff"/></svg>
    <span class="service-label">EXTERIOR</span>
  </div>
  <div class="abs service" style="left:380px">
    <svg width="210" height="210"><circle cx="105" cy="105" r="92" fill="none" stroke="#6fb1ad" stroke-width="14"/>
      <rect x="84" y="80" width="34" height="18" rx="4" fill="#6fb1ad"/><rect x="80" y="92" width="42" height="12" rx="3" fill="#6fb1ad"/><rect x="130" y="70" width="3" height="34" fill="#6fb1ad"/><path d="M124 70 L139 70 L135 62 L128 62 Z" fill="#6fb1ad"/></svg>
    <span class="service-label">INTERIOR</span>
  </div>
  <div class="abs service" style="left:600px">
    <svg width="210" height="210"><circle cx="105" cy="105" r="92" fill="none" stroke="#6f7fc4" stroke-width="14"/>
      <path d="M78 84 L105 62 L132 84 L132 106 L78 106 Z" fill="#6f7fc4"/><rect x="88" y="88" width="8" height="8" fill="#fff"/><rect x="114" y="88" width="8" height="8" fill="#fff"/><rect x="101" y="94" width="8" height="12" fill="#fff"/></svg>
    <span class="service-label">RESIDENTIAL</span>
  </div>
  <div class="abs service" style="left:822px">
    <svg width="210" height="210"><circle cx="105" cy="105" r="92" fill="none" stroke="#e86a9b" stroke-width="14"/>
      <rect x="88" y="64" width="22" height="42" fill="#e86a9b"/><rect x="110" y="80" width="18" height="26" fill="#e86a9b"/>
      <g fill="#fff"><rect x="92" y="70" width="5" height="5"/><rect x="101" y="70" width="5" height="5"/><rect x="92" y="80" width="5" height="5"/><rect x="101" y="80" width="5" height="5"/><rect x="92" y="90" width="5" height="5"/><rect x="101" y="90" width="5" height="5"/><rect x="115" y="86" width="5" height="5"/><rect x="115" y="95" width="5" height="5"/></g></svg>
    <span class="service-label">COMMERCIAL</span>
  </div>
</section>

<section class="abs feature">
  <span class="pointer"></span>
  <div class="abs feature-panel">
    <h3>EXTERIOR</h3>
    <h2>PAINTING</h2>
    <p>Sed ut perspiciatis unde omnis iste natus error sit voluptatem accudf dgsantium doloremque laudantium, totam rem aperiam, eaque ipsa quae ab illo inventore veritatis et quasi architecto beatae vitae dicta sunt explicabo. Nemo enim ipsam voluptatem quia voluptas sit aspernatur aut odit aut fudgit, sed quia cfdonsequ untur magni dolores eos qui ratione voluptatem sequi nesdfciunt. Neque porro quisquam est, qui dolorem ipsum quia dolor sit amet, consectetur, adipisci velit, sed quia non numquam eius modi tempor.</p>
    <span class="btn">Read More</span>
    <div class="abs feature-photo" role="img" aria-label="Photo of a painter on scaffolding painting a white exterior wall"></div>
  </div>
</section>

<section class="abs projects">
  <h2 class="section-title">Our Latest Projects</h2>
  <svg class="abs arrow" style="left:116px" width="22" height="46"><path d="M20 2 L3 23 L20 44" fill="none" stroke="#bbb" stroke-width="2"/></svg>
  <svg class="abs arrow" style="left:1060px" width="22" height="46"><path d="M2 2 L19 23 L2 44" fill="none" stroke="#bbb" stroke-width="2"/></svg>
  <article class="abs project" style="left:155px">
    <div class="project-img" role="img" aria-label="Photo of a bedroom with red feature walls" style="background:linear-gradient(135deg,#b9303a,#d9d2cb 60%,#7a6a62)"></div>
    <h4>LOREM IPSUM DOLOR SIT AMET</h4>
    <p>Radipiscing elit, sed do eiusmod tempr incididunt ut labore et dolore majhkna aliqua. Ut enim ad minim veniam, quis nostrud exercitation ullamco laborisut aliquip ex ea commodo cons.</p>
    <span class="btn">Read More</span>
  </article>
  <article class="abs project" style="left:382px">
    <div class="project-img" role="img" aria-label="Black and white photo of a suburban house" style="background:linear-gradient(135deg,#d8d8d8,#7b7b7b 60%,#444)"></div>
    <h4>LOREM IPSUM DOLOR SIT AMET</h4>
    <p>Radipiscing elit, sed do eiusmod tempor incididunt ut labore et dolore majhkna aliqua. Ut enim ad minim veniam, quis nostrud exercitation ullamco laborisut aliquip ex ea commodo cons.</p>
    <span class="btn muted">Read More</span>
  </article>
  <article class="abs project" style="left:608px">
    <div class="project-img" role="img" aria-label="Photo of a living room with orange and yellow walls" style="background:linear-gradient(135deg,#e2541f,#f0a436 55%,#e8dccb)"></div>
    <h4>LOREM IPSUM DOLOR SIT AMET</h4>
    <p>Radipiscing elit, sed do eiusmod incidid unt ut labore et dolore majhkna aliqua. Ut enim ad minim veniam, quis nostrud exercitation ullamco laborisut aliquip ex ea commodo cons.</p>
    <span class="btn">Read More</span>
  </article>
  <article class="abs project" style="left:835px">
    <div class="project-img" role="img" aria-label="Photo of a single-storey house with a front lawn" style="background:linear-gradient(180deg,#8fb3d9,#6d7480 50%,#4f7d3c)"></div>
    <h4>LOREM IPSUM DOLOR SIT AMET</h4>
    <p>Radipiscing elit, sed do eiusmod tepor incididunt ut labore et dolore majhkna aliqua. Ut enim ad minim veniam, quis nostrud exercitation ullamco laborisut aliquip ex ea commodo cons.</p>
    <span class="btn">Read More</span>
  </article>
</section>

<section class="abs news">
  <h2 class="section-title">Latest News</h2>
  <div class="abs news-arrows">
    <svg width="12" height="20"><path d="M10 2 L3 10 L10 18" fill="none" stroke="#999" stroke-width="1.5"/></svg>
    <svg width="12" height="20"><path d="M2 2 L9 10 L2 18" fill="none" stroke="#999" stroke-width="1.5"/></svg>
  </div>
  <article class="abs news-item" style="left:162px;top:100px">
    <div class="news-date"><b>10</b><small>JUNE</small></div>
    <h5>LOREM IPSUM DOLOR SIT AMET</h5>
    <p>Neque porro quisquam est, qui dolorem ipsum quia dolor sit amet, consdfgs porro quisquam est, qui dolorem</p>
    <a>- READ MORE</a>
  </article>
  <article class="abs news-item" style="left:459px;top:100px">
    <div class="news-date"><b style="color:#fff;background:var(--blue)">15</b><small style="background:var(--blue-dark)">JUNE</small></div>
    <h5>LOREM IPSUM DOLOR SIT AMET</h5>
    <p>Neque porro quisquam est, qui dolorem ipsum quia dolor sit amet, consdfgs porro quisquam est, qui dolorem</p>
    <a>- READ MORE</a>
  </article>
  <div class="abs news-rule"></div>
  <article class="abs news-item" style="left:162px;top:240px">
    <div class="news-date"><b>18</b><small>JUNE</small></div>
    <h5>LOREM IPSUM DOLOR SIT AMET</h5>
    <p>Neque porro quisquam est, qui dolorem ipsum quia dolor sit amet, consdfgs porro quisquam est, qui dolorem</p>
    <a>- READ MORE</a>
  </article>
  <article class="abs news-item" style="left:459px;top:240px">
    <div class="news-date"><b>20</b><small>JUNE</small></div>
    <h5>LOREM IPSUM DOLOR SIT AMET</h5>
    <p>Neque porro quisquam est, qui dolorem ipsum quia dolor sit amet, consdfgs porro quisquam est, qui dolorem</p>
    <a>- READ MORE</a>
  </article>
  <form class="abs quick-contact">
    <h3>QUICK CONTACT</h3>
    <input type="text" placeholder="Name">
    <input type="text" placeholder="Mobile">
    <input type="text" placeholder="E-mail">
    <textarea placeholder="Message"></textarea>
    <button type="button">SUBMIT</button>
  </form>
</section>

<footer class="abs site-footer">
  <div class="social"><span></span><span></span><span></span><span></span></div>
  <p>© 2015. <b>Bluefinch Painting.</b> All rights reserved.</p>
  <div class="rainbow"></div>
</footer>

</body>
</html>
```